Domain Parking page and Listing page

1)
In need a design of a domain parking page, mainly with the same features as VORIQ.com as can be seen here: https://wanderplum.com/

2)
I need a design of a website with all domains listed. There's no company logo/name yet so it should be in plain font, for example "tilmorex.site" (this is just an example), similar as:
https://voriq.com/search?&terms=park&results=50&order_by=relevance

Delivery after approval in HTML/CSS. Should be responsive. Ideally use a framework like Bootstrap

Target Market(s)

Domain buyers, business owners

Industry/Entity Type

Business to business, Marketing, domains

Coding

Coded - Design and coding required

Number of Pages Required

2 page

Font styles to use
Sans Serif

Requirements
Must have
• Responsive design, worldly design.

```html
<!DOCTYPE html>
<html lang="en">
<head>
<meta charset="utf-8">
<title>tilmorex.site — parking and listing pages</title>
<link href="https://fonts.googleapis.com/css2?family=Plus+Jakarta+Sans:wght@400;500;600;700;800&display=swap" rel="stylesheet">
<style>
:root{
  --ink:#0d1530;
  --navy:#081433;
  --blue:#2a8cf7;
  --blue-2:#0bc8fb;
  --blue-3:#5b8bf7;
  --sky:#d8efff;
  --board:#dde6f2;
  --grey:#6b7385;
  --line:#e3e8f0;
  --card:#ffffff;
}
*{box-sizing:border-box;margin:0;padding:0}
html,body{width:851px;height:1200px;overflow:hidden;background:var(--board)}
body{font-family:"Plus Jakarta Sans",Arial,sans-serif;color:var(--ink)}
.board{position:absolute;left:0;top:0;width:1624px;height:2290px;transform:scale(.52401);transform-origin:0 0;background:var(--board);overflow:hidden}
.board-waves{position:absolute;inset:0}
.board-title{position:absolute;top:90px;left:0;width:100%;text-align:center;font-size:82px;font-weight:800;letter-spacing:-1px}
.page{position:absolute;width:656px;overflow:hidden;background:#f1f6fd;box-shadow:0 10px 40px rgba(40,70,120,.12)}
.page--home{left:136px;top:248px;height:1950px}
.page--listing{left:832px;top:248px;height:1477px}
.abs{position:absolute}
.hero-bg{position:absolute;left:0;top:0;width:656px}
.brand{position:absolute;left:48px;top:14px;font-size:13px;font-weight:700}
.nav{position:absolute;left:289px;top:17px;display:flex;gap:9px;font-size:7.5px;font-weight:500}
.nav .active{color:var(--blue)}
.nav-mark{position:absolute;left:288px;top:0;width:26px;height:3px;border-radius:0 0 3px 3px;background:var(--blue)}
.btn-login{position:absolute;left:549px;top:12px;width:58px;height:22px;border-radius:11px;background:var(--blue);color:#fff;font-size:7px;font-weight:800;display:flex;align-items:center;justify-content:center}
.search{position:absolute;background:#fff;border-radius:20px;box-shadow:0 4px 14px rgba(40,90,160,.15);display:flex;align-items:center;padding-left:12px;font-size:8px;color:var(--grey)}
.search .go{position:absolute;right:5px;top:50%;transform:translateY(-50%);border-radius:50%;background:var(--blue);display:flex;align-items:center;justify-content:center}
.art{position:absolute;border-radius:18px}
.hero-welcome{position:absolute;left:49px;top:105px;font-size:16px;font-weight:700}
.hero-brand{position:absolute;left:48px;top:122px;font-size:40px;font-weight:800;letter-spacing:-.5px}
.hero-claim{position:absolute;left:49px;top:178px;font-size:17px;font-weight:500;line-height:21px}
.hero-sub{position:absolute;left:49px;top:226px;font-size:10px;color:#3e4760}
.scroll-down{position:absolute;left:55px;top:340px;width:52px;height:52px;border-radius:50%;background:#fff;box-shadow:0 6px 18px rgba(40,90,160,.15);display:flex;align-items:center;justify-content:center}
.card{position:absolute;top:540px;width:131px;height:163px;background:var(--card);border-radius:8px;box-shadow:0 6px 22px rgba(40,90,160,.1);text-align:center}
.card .icon{width:40px;height:36px;margin:18px auto 0;border:2px solid var(--blue);border-radius:8px;background:#e8f3ff}
.card h3{font-size:9.5px;font-weight:800;line-height:12px;margin-top:11px}
.card p{font-size:6.3px;color:var(--grey);line-height:10.5px;margin:6px 14px 0}
.card .more{position:absolute;left:10px;right:10px;bottom:7px;border-top:1px solid var(--line);padding-top:9px;font-size:6.3px;font-weight:800}
.h2{position:absolute;font-weight:800;letter-spacing:-.3px}
.para{position:absolute;font-size:7.3px;color:var(--grey);line-height:11px}
.feat{position:absolute;left:382px;width:220px}
.feat h4{font-size:9.5px;font-weight:800}
.feat p{font-size:5.8px;color:var(--grey);line-height:9.5px;margin-top:3px;padding-left:8px;position:relative}
.feat p::before{content:"";position:absolute;left:0;top:3px;width:4px;height:4px;border-radius:50%;background:var(--blue)}
.btn{position:absolute;border-radius:14px;background:linear-gradient(90deg,var(--blue-3),var(--blue));color:#fff;font-size:7px;font-weight:800;display:flex;align-items:center;justify-content:center}
.video{position:absolute;left:100px;top:1062px;width:455px;height:243px;border-radius:10px;background:#eceff4;overflow:hidden}
.play{position:absolute;left:306px;top:163px;width:44px;height:44px;border-radius:50%;background:var(--blue);display:flex;align-items:center;justify-content:center}
.cta{position:absolute;left:93px;width:470px;height:105px;border-radius:52px;background:linear-gradient(90deg,var(--blue-3),var(--blue-2));text-align:center;color:#fff}
.cta h2{font-size:20px;font-weight:800;margin-top:20px}
.cta p{font-size:7.5px;margin-top:4px}
.cta .search{left:128px;top:68px;width:214px;height:22px;padding-left:10px;font-size:7.5px}
.footer-bg{position:absolute;left:0;width:656px}
.f-brand{position:absolute;left:78px;font-size:16px;font-weight:800;color:#fff}
.socials{position:absolute;left:100px;display:flex;gap:6px}
.socials span{width:11px;height:11px;border-radius:50%;background:#2a3557}
.f-col{position:absolute;color:#fff}
.f-col h5{font-size:9px;font-weight:700;margin-bottom:4px}
.f-col a{display:block;font-size:6.3px;line-height:13.5px;color:#c7cede;text-decoration:none}
.f-rule{position:absolute;left:52px;width:558px;height:1px;background:#27345a}
.f-copy{position:absolute;left:0;width:656px;text-align:center;color:#fff;font-size:6.3px;font-weight:600}
.to-top{position:absolute;left:614px;width:22px;height:22px;border-radius:50%;background:var(--blue);display:flex;align-items:center;justify-content:center}
.listing-title{position:absolute;left:0;width:656px;text-align:center;top:82px;font-size:40px;font-weight:800}
.filters{position:absolute;left:113px;top:326px;display:flex;gap:9px;font-size:8.5px;font-weight:700}
.filters span::after{content:" ⌄";color:var(--blue);font-size:7px}
.checks{position:absolute;left:163px;top:369px;display:flex;gap:11px;font-size:8.5px}
.checks span{display:flex;align-items:center;gap:4px}
.checks i{width:10px;height:10px;border:1.2px solid #333;border-radius:2px;display:inline-block}
.ext-input{position:absolute;left:310px;top:364px;width:180px;height:22px;background:#fff;border-radius:11px;font-size:7px;color:var(--grey);padding:6px 12px}
.plus{position:absolute;left:471px;top:366px;width:18px;height:18px;border-radius:50%;background:var(--blue);color:#fff;font-size:13px;line-height:17px;text-align:center}
.results{position:absolute;left:48px;top:416px;font-size:9px;font-weight:800}
.results small{font-size:7px;font-weight:500}
.sort-label{position:absolute;left:450px;top:417px;font-size:7px;color:var(--grey)}
.sort{position:absolute;left:482px;top:410px;width:125px;height:22px;border-radius:11px;background:#fff;box-shadow:0 3px 10px rgba(40,90,160,.1);font-size:6.5px;padding:7px 10px;color:#3e4760}
.rule{position:absolute;height:1px;background:var(--line)}
.chosen{position:absolute;left:219px;top:465px;font-size:6.8px;font-weight:700}
.chip{position:absolute;left:290px;top:458px;width:85px;height:20px;border-radius:10px;background:#e8edf5;font-size:6.8px;font-weight:700;text-align:center;line-height:20px}
.reset{position:absolute;left:393px;top:465px;font-size:6.8px;color:var(--blue);font-weight:700}
.row{position:absolute;left:48px;width:559px;height:47px;border-bottom:1px solid var(--line)}
.row b{position:absolute;left:0;top:3px;font-size:11.5px;font-weight:800}
.row em{position:absolute;left:0;top:19px;font-size:7px;font-style:normal;color:#3e4760;padding-left:7px}
.row em::before{content:"";position:absolute;left:0;top:2.5px;width:4px;height:4px;border-radius:50%;background:var(--blue)}
.pill{position:absolute;top:4px;width:69px;height:22px;border:1px solid #1b2440;border-radius:11px;font-size:6.2px;font-weight:800;display:flex;align-items:center;justify-content:center;background:#fff}
.pill.action{left:490px}
.pill.p2{left:412px}
.pill.p1{left:322px}
.or{position:absolute;left:396px;top:12px;font-size:5.5px;color:#9aa1b0}
.pager{position:absolute;top:1083px;font-size:9px;font-weight:600}
.pg-btn{position:absolute;top:1084px;height:22px;border-radius:11px;font-size:8px;font-weight:800;display:flex;align-items:center;justify-content:center}
</style>
</head>
<body>
<div class="board">
  <svg class="board-waves" width="1624" height="2290" viewBox="0 0 1624 2290" aria-hidden="true">
    <path d="M0 580 C300 560 500 640 800 660 S1300 600 1624 560 L1624 2290 L0 2290Z" fill="#eef1f6"/>
    <path d="M0 1700 C300 1650 600 1880 900 1860 S1400 1700 1624 1680 L1624 2290 L0 2290Z" fill="#f4f4f4"/>
    <path d="M0 2000 C400 1900 700 2150 1100 2080 S1500 1980 1624 2000 L1624 2290 L0 2290Z" fill="#dfe6f1"/>
  </svg>
  <h1 class="board-title">tilmorex.site</h1>

  <!-- Home page -->
  <section class="page page--home">
    <svg class="hero-bg" height="500" viewBox="0 0 656 500" aria-hidden="true">
      <defs><linearGradient id="hg" x1="0" y1="0" x2="0" y2="1"><stop offset="0" stop-color="#eef4fd"/><stop offset="1" stop-color="#dff2ff"/></linearGradient></defs>
      <rect width="656" height="500" fill="url(#hg)"/>
      <path d="M0 400 C120 380 180 470 300 480 S500 400 656 440 L656 500 L0 500Z" fill="#f1f6fd"/>
    </svg>
    <div class="nav-mark"></div>
    <div class="brand">tilmorex.site</div>
    <nav class="nav"><span class="active">Home</span><span>Buy a domain</span><span>Sell your domain</span><span>Learn</span><span>Company</span></nav>
    <div class="btn-login">LOG IN</div>

    <div class="hero-welcome">Welcome to</div>
    <div class="hero-brand">tilmorex</div>
    <div class="hero-claim">Claim your space in the<br>digital world</div>
    <div class="hero-sub">Premium hosting for everyone, small or large</div>
    <div class="search" style="left:49px;top:254px;width:238px;height:28px">Think of a domain name<span class="go" style="width:19px;height:19px"><svg width="8" height="8" viewBox="0 0 10 10"><circle cx="4" cy="4" r="3" fill="none" stroke="#fff" stroke-width="1.5"/><path d="M6.3 6.3 9 9" stroke="#fff" stroke-width="1.5"/></svg></span></div>
    <div class="scroll-down"><svg width="12" height="8" viewBox="0 0 12 8"><path d="M1 1l5 5 5-5" fill="none" stroke="var(--blue)" stroke-width="1.8"/></svg></div>
    <div class="art" role="img" aria-label="Illustration of a person with a magnifying glass beside a browser search window, rocket and folders" style="left:335px;top:45px;width:315px;height:320px;background:linear-gradient(160deg,#e6eef9,#cfe3fb 60%,#b9d6fb)"></div>

    <div class="card" style="left:125px"><div class="icon" role="img" aria-label="Web address search icon"></div><h3>Popular domain<br>names</h3><p>Take a look at the most popular domain names. And buy them immediately…</p><div class="more">READ MORE</div></div>
    <div class="card" style="left:263px"><div class="icon" role="img" aria-label="Web link icon"></div><h3>3-letter domain<br>names</h3><p>3-letter domain names are short, sweet, and super easy to remember. Check…</p><div class="more">READ MORE</div></div>
    <div class="card" style="left:400px"><div class="icon" role="img" aria-label="Globe icon"></div><h3>Premium domain<br>names</h3><p>Premium domain names are usually short, easy to brand, and use a popular…</p><div class="more">READ MORE</div></div>

    <div class="art" role="img" aria-label="Illustration of a woman at a laptop surrounded by browser windows and a globe" style="left:48px;top:765px;width:312px;height:240px;background:linear-gradient(150deg,#eef2f8,#d6e4f6)"></div>
    <div class="h2" style="left:382px;top:766px;font-size:20px">Buy and sell domains</div>
    <p class="para" style="left:382px;top:800px;width:225px">VORIQ.com is a marketplace for domain names. We make sure buying, selling and transferring domains goes smoothly and hassle-free.</p>
    <div class="feat" style="top:842px"><h4>Transparency first</h4><p>No hidden costs. No complicated math. You'll never be in the dark, whether you're buying or selling.</p></div>
    <div class="feat" style="top:883px"><h4>Effortless trading</h4><p>By using state of the art technology, domain name trading is super simple thanks to our easy-to-use platform.</p></div>
    <div class="feat" style="top:924px"><h4>Secure transactions</h4><p>Security is important to us. Our fraud prevention team monitors all transactions &amp; keeps you safe.</p></div>
    <div class="btn" style="left:382px;top:968px;width:93px;height:24px">GET TO KNOW US</div>

    <div class="h2" style="left:0;width:656px;text-align:center;top:1028px;font-size:19px">Watch my video</div>
    <div class="video">
      <div class="abs" role="img" aria-label="Illustration of a person walking past a browser window with a web search" style="left:115px;top:20px;width:230px;height:210px;border-radius:50%;background:#e0e4eb"></div>
      <div class="play"><svg width="14" height="16" viewBox="0 0 14 16"><path d="M2 1l11 7-11 7z" fill="#fff"/></svg></div>
    </div>

    <div class="h2" style="left:87px;top:1386px;font-size:21px;line-height:25px">Here for domain<br>investors too</div>
    <p class="para" style="left:88px;top:1442px;width:198px">As a domain investor, you have particular needs. We get it! So we built a special platform just for domain investors. With its clear interface, bulk domain name uploading and editing features, selling is easier than ever.</p>
    <div class="btn" style="left:88px;top:1510px;width:130px;height:26px">DISCOVER OUR PLATFORM</div>
    <div class="art" role="img" aria-label="Illustration of two people beside a registration panel listing domain extensions" style="left:300px;top:1365px;width:265px;height:195px;background:linear-gradient(150deg,#e8eef8,#d3e3f7)"></div>

    <svg class="footer-bg" style="top:1660px" height="290" viewBox="0 0 656 290" aria-hidden="true"><path d="M0 80 C120 40 200 60 330 70 S560 40 656 20 L656 290 L0 290Z" fill="var(--navy)"/></svg>
    <div class="cta" style="top:1610px"><h2>Build your online business</h2><p>Lay a solid foundation for your business with a killer domain name.</p><div class="search">Think of a domain name<span class="go" style="width:16px;height:16px"><svg width="7" height="7" viewBox="0 0 10 10"><circle cx="4" cy="4" r="3" fill="none" stroke="#fff" stroke-width="1.5"/><path d="M6.3 6.3 9 9" stroke="#fff" stroke-width="1.5"/></svg></span></div></div>
    <div class="f-brand" style="top:1822px">tilmorex.site</div>
    <div class="socials" style="top:1854px"><span></span><span></span><span></span><span></span><span></span></div>
    <div class="f-col" style="left:238px;top:1798px"><h5>Quick Link</h5><a>Home</a><a>Buy a domain</a><a>Sell your domain</a><a>Learn</a><a>Company</a></div>
    <div class="f-col" style="left:326px;top:1798px"><h5>Information</h5><a>Privacy policy</a><a>Terms and condition</a><a>Disclamier</a><a>Sitemap</a></div>
    <div class="f-col" style="left:434px;top:1798px"><h5>Serclves</h5><a>Buy a domain</a><a>Sell your<br>domain</a><a>API Partnership<br>Program</a><a>Brokerage</a></div>
    <div class="f-col" style="left:522px;top:1798px"><h5>Learn</h5><a>News</a><a>Trust &amp; Security</a><a>Help center</a><a>Transaction</a><a>explorer</a></div>
    <div class="f-rule" style="top:1905px"></div>
    <div class="f-copy" style="top:1931px">© Copyright 2023 tilmorex.site | All Right Reserveds</div>
    <div class="to-top" style="top:1912px"><svg width="8" height="6" viewBox="0 0 8 6"><path d="M1 5l3-3 3 3" fill="none" stroke="#fff" stroke-width="1.4"/></svg></div>
  </section>

  <!-- Listing page -->
  <section class="page page--listing">
    <svg class="hero-bg" height="330" viewBox="0 0 656 330" aria-hidden="true">
      <rect width="656" height="330" fill="#eef4fd"/>
      <path d="M0 160 C80 140 160 170 260 230 S420 320 520 260 S620 170 656 160 L656 330 L0 330Z" fill="#dcf1ff"/>
      <path d="M0 250 C120 230 220 300 330 310 S520 260 656 280 L656 330 L0 330Z" fill="#f1f6fd"/>
    </svg>
    <div class="nav-mark"></div>
    <div class="brand">tilmorex.site</div>
    <nav class="nav"><span class="active">Home</span><span>Buy a domain</span><span>Sell your domain</span><span>Learn</span><span>Company</span></nav>
    <div class="btn-login">LOG IN</div>
    <h1 class="listing-title">Listing</h1>
    <div class="search" style="left:155px;top:146px;width:345px;height:32px;color:#3e4760">park<span class="go" style="width:21px;height:21px"><svg width="8" height="8" viewBox="0 0 10 10"><circle cx="4" cy="4" r="3" fill="none" stroke="#fff" stroke-width="1.5"/><path d="M6.3 6.3 9 9" stroke="#fff" stroke-width="1.5"/></svg></span></div>

    <div class="filters"><span>Categories</span><span>Extensions</span><span>Length</span><span>Price</span><span>Name</span><span>Starting with</span><span>Ending with</span></div>
    <div class="checks"><span><i></i>.com</span><span><i></i>.net</span><span><i></i>.org</span></div>
    <div class="ext-input">add extension</div>
    <div class="plus">+</div>
    <div class="results">28700 <small>results</small></div>
    <div class="sort-label">Sort by</div>
    <div class="sort">Relevance High - Low</div>
    <div class="rule" style="left:48px;top:443px;width:559px"></div>
    <div class="chosen">Chosen filters:</div>
    <div class="chip">contains: park ✕</div>
    <div class="reset">Reset filters</div>

    <div class="row" style="top:503px"><b>park.amsterdam</b><em>Canalline BV</em><span class="pill action">MAKE OFFER</span></div>
    <div class="row" style="top:550px"><b>park.frl</b><em>Frisreg BV</em><span class="pill action">MAKE OFFER</span></div>
    <div class="row" style="top:598px"><b>park.com.ar</b><em>Domvale.com</em><span class="pill p1">$1,307</span><span class="or">OR</span><span class="pill p2">$103/month</span><span class="pill action">BUY NOW</span></div>
    <div class="row" style="top:646px"><b>park.eco</b><em>Green Hall, the .eco registry</em><span class="pill action">MAKE OFFER</span></div>
    <div class="row" style="top:694px"><b>park.al</b><em>AR</em><span class="pill action">MAKE OFFER</span></div>
    <div class="row" style="top:742px"><b>park.market</b><em>Marten Hollis</em><span class="pill action">MAKE OFFER</span></div>
    <div class="row" style="top:790px"><b>park.cat</b><em>Domain seller</em><span class="pill action">BUY NOW</span></div>
    <div class="row" style="top:838px"><b>park.promo</b><em>Domain seller</em><span class="pill action">MAKE OFFER</span></div>
    <div class="row" style="top:886px"><b>park.trade</b><em>7.prime</em><span class="pill p2">$4,999</span><span class="pill action">BUY NOW</span></div>
    <div class="row" style="top:934px"><b>park.do</b><em>Domain seller</em><span class="pill p2">$100,000</span><span class="pill action">BUY NOW</span></div>
    <div class="row" style="top:982px"><b>park.click</b><em>Netward Holdings</em><span class="pill action">MAKE OFFER</span></div>
    <div class="row" style="top:1030px;border-bottom:0"><b>park.cl</b><em>Domvale.com</em><span class="pill p1">$1,742</span><span class="or">OR</span><span class="pill p2">$101/month</span><span class="pill action">BUY NOW</span></div>

    <div class="pg-btn" style="left:186px;width:60px;background:#e8edf5">‹ PREV</div>
    <div class="pager" style="left:274px">1</div>
    <div class="abs" style="left:293px;top:1084px;width:22px;height:22px;border-radius:50%;background:var(--navy);color:#fff;font-size:9px;font-weight:700;text-align:center;line-height:22px">2</div>
    <div class="pager" style="left:331px">3</div>
    <div class="pager" style="left:350px">…</div>
    <div class="pager" style="left:369px">576</div>
    <div class="pg-btn" style="left:410px;width:60px;background:var(--blue);color:#fff">NEXT ›</div>

    <svg class="footer-bg" style="top:1180px" height="297" viewBox="0 0 656 297" aria-hidden="true"><path d="M0 60 C60 20 120 30 200 50 S500 110 656 70 L656 297 L0 297Z" fill="var(--navy)"/></svg>
    <div class="cta" style="top:1138px"><h2>Build your online business</h2><p>Lay a solid foundation for your business with a killer domain name.</p><div class="search">Think of a domain name<span class="go" style="width:16px;height:16px"><svg width="7" height="7" viewBox="0 0 10 10"><circle cx="4" cy="4" r="3" fill="none" stroke="#fff" stroke-width="1.5"/><path d="M6.3 6.3 9 9" stroke="#fff" stroke-width="1.5"/></svg></span></div></div>
    <div class="f-brand" style="top:1350px">tilmorex.site</div>
    <div class="socials" style="top:1382px"><span></span><span></span><span></span><span></span><span></span></div>
    <div class="f-col" style="left:238px;top:1326px"><h5>Quick Link</h5><a>Home</a><a>Buy a domain</a><a>Sell your domain</a><a>Learn</a><a>Company</a></div>
    <div class="f-col" style="left:326px;top:1326px"><h5>Information</h5><a>Privacy policy</a><a>Terms and condition</a><a>Disclamier</a><a>Sitemap</a></div>
    <div class="f-col" style="left:434px;top:1326px"><h5>Serclves</h5><a>Buy a domain</a><a>Sell your<br>domain</a><a>API Partnership<br>Program</a><a>Brokerage</a></div>
    <div class="f-col" style="left:522px;top:1326px"><h5>Learn</h5><a>News</a><a>Trust &amp; Security</a><a>Help center</a><a>Transaction</a><a>explorer</a></div>
    <div class="f-rule" style="top:1452px"></div>
    <div class="f-copy" style="top:1460px">© Copyright 2023 tilmorex.site | All Right Reserveds</div>
    <div class="to-top" style="top:1440px"><svg width="8" height="6" viewBox="0 0 8 6"><path d="M1 5l3-3 3 3" fill="none" stroke="#fff" stroke-width="1.4"/></svg></div>
  </section>
</div>
</body>
</html>
```